Modern Fun Bold Laundry stain remover wipes and spray

Marlo Goods packaging is bold, modern, and unapologetically real—just like the messes it’s made to handle.
please look at brand guidelines for colours and text etc. Please also just use sample text where descriptions etc need to go on packaging and i will fill in later.
3 die lines. 1 a box that will contain wipes - one the wipe packet and another is just sticker that will go on stain remover spray bottle

The design is clean but not precious. High contrast colors, strong typography, and plenty of breathing room give it a confident, fast-acting feel. The look says effective first, aesthetic second—but still looks damn good on a shelf or in a laundry room.

Typography is strong, modern, and slightly irreverent. Large, clear headlines deliver attitude up front, while short punchy lines replace traditional cleaning jargon. No scripts, no frills—just bold sans-serif type that feels sharp, capable, and honest.

Copy is conversational and fearless:

Speaks directly to the customer

Acknowledges real messes (stains, spills, toilets)

Never sugarcoats or over-explains

Confident without being aggressive

Funny without trying too hard

Visual elements are minimal but intentional—simple icons, soapy suds, bubbles, subtle texture, laundry tile feel or graphic blocks that hint at motion and speed. Nothing fussy. Nothing “clinical.” This is modern utility with personality.

The overall tone:

Fun but tough

Edgy but trustworthy

Modern without being cold

Relatable without being messy

Marlo doesn’t promise perfection—she promises results.

Shelf presence: bold, eye-catching, and instantly legible from a distance.
In-hand feel: sturdy, practical, and premium without being precious.
Brand energy: “I’ve got this.”

Get it dirty. Marlo will clean it.

logo, die lines and all ideas i like are uploaded

Target Market(s)

28-48 women

Industry/Entity Type

laundry cleaning

Font styles to use
Other font styles liked:
• all fonts and colours are in brand guidelines

Requirements
Must have
• Die line box - Front - Logo, Stain remover, Fast and effective, for clothes fabric and on the go messes, 25 wipes inside. Sides - ecofriendly, fast and effective, no harsh chemicals, Vegan, travel friendly, other side a fun tagline. Back. please just put sample text I will put proper text in
Should not have
• be boring an original

```html
<!DOCTYPE html>
<html lang="en">
<head>
<meta charset="utf-8">
<title>Marlo Goods – Stain Remover Packaging</title>
<link rel="stylesheet" href="https://fonts.googleapis.com/css2?family=Source+Serif+4:wght@400;600;700;800&family=Open+Sans:wght@400;600;700&display=swap">
<style>
  :root {
    --stage: #b7b9fb;
    --label-deep: #5a4fd3;
    --label-mid: #7d74e8;
    --label-light: #b5aef9;
    --box-face: #7f7cec;
    --box-side: #6f69dc;
    --box-top: #7770e4;
    --brand-green: #1e4a33;
    --ink: #2b2a44;
    --ink-soft: #3d3b5c;
    --badge-gold: #8c8a3a;
  }
  * { box-sizing: border-box; margin: 0; padding: 0; }
  html, body { width: 1200px; height: 848px; overflow: hidden; }
  body {
    background: var(--stage);
    font-family: "Open Sans", sans-serif;
    color: var(--ink);
    position: relative;
  }

  .panel { position: absolute; overflow: hidden; }
  .decor { position: absolute; inset: 0; width: 100%; height: 100%; pointer-events: none; }
  .abs { position: absolute; left: 0; right: 0; text-align: center; white-space: nowrap; }

  .brand-name {
    font-family: "Source Serif 4", serif;
    font-weight: 800;
    color: var(--brand-green);
    letter-spacing: -1px;
    line-height: 1;
  }
  .product-type {
    font-family: "Source Serif 4", serif;
    font-weight: 600;
    color: var(--ink);
    text-transform: uppercase;
    line-height: 1;
  }
  .headline {
    font-family: "Source Serif 4", serif;
    font-weight: 600;
    color: var(--ink);
    line-height: 1;
  }
  .tagline {
    font-family: "Source Serif 4", serif;
    font-weight: 600;
    color: var(--ink-soft);
    line-height: 1;
  }
  .eco-badge {
    position: absolute;
    border-radius: 50%;
    border: 2px solid var(--badge-gold);
    background: rgba(255,255,255,0.08);
  }
  .volume {
    position: absolute;
    display: flex;
    border: 2px solid var(--brand-green);
    font-family: "Open Sans", sans-serif;
    line-height: 1;
  }
  .volume span { padding: 3px 8px; }
  .volume .volume-alt { color: var(--ink); }
  .volume .volume-main { background: var(--brand-green); color: #fff; }

  /* Spray front label */
  .label-front {
    left: 87px; top: 426px; width: 285px; height: 260px;
    background: linear-gradient(90deg, var(--label-mid) 0%, var(--label-deep) 55%, var(--label-light) 100%);
  }
  .label-front .brand-name { top: 58px; font-size: 48px; }
  .label-front .product-type { top: 110px; font-size: 12px; }
  .label-front .headline { top: 137px; font-size: 25px; }
  .label-front .tagline { top: 173px; font-size: 14px; }
  .label-front .eco-badge { left: 22px; top: 202px; width: 46px; height: 46px; }
  .label-front .volume { left: 92px; top: 214px; font-size: 11px; }

  /* Spray back label */
  .label-back {
    left: 442px; top: 426px; width: 285px; height: 260px;
    background: linear-gradient(90deg, var(--label-mid) 0%, var(--label-light) 40%, var(--label-deep) 75%, var(--label-light) 100%);
    padding: 10px 38px 0 31px;
    font-size: 6.3px;
    line-height: 1.35;
    color: var(--ink-soft);
  }
  .label-back .brand-name { font-size: 24px; margin-left: 43px; }
  .label-back .product-type { font-size: 7px; margin-left: 43px; margin-top: 5px; }
  .info-block { margin-top: 8px; text-align: justify; }
  .info-block strong { color: var(--ink); font-weight: 700; }
  .label-back .info-block.first { margin-top: 13px; }

  /* Wipes box – top flap */
  .box-top {
    left: 880px; top: 150px; width: 290px; height: 150px;
    background: var(--box-top);
  }
  .box-top .brand-name { top: 22px; font-size: 42px; }
  .box-top .product-type { top: 68px; font-size: 10px; }
  .box-top .headline { top: 86px; font-size: 21px; }
  .box-top .tagline { top: 114px; font-size: 12px; color: var(--ink); }

  /* Wipes box – side */
  .box-side {
    left: 760px; top: 300px; width: 120px; height: 310px;
    background: var(--box-side);
    padding: 16px 10px 0 10px;
    font-size: 5px;
    line-height: 1.35;
    color: var(--ink);
  }
  .box-side .brand-name { font-size: 22px; }
  .box-side .product-type { font-size: 5.5px; margin-top: 3px; }
  .box-side .info-block { margin-top: 6px; }
  .box-side .info-block.first { margin-top: 12px; }

  /* Wipes box – front */
  .box-front {
    left: 880px; top: 300px; width: 290px; height: 310px;
    background: var(--box-face);
  }
  .box-front .brand-name { top: 72px; font-size: 62px; }
  .box-front .product-type { top: 140px; font-size: 13px; }
  .box-front .headline { top: 170px; font-size: 30px; }
  .box-front .tagline { top: 213px; font-size: 15px; color: var(--ink); }
  .box-front .eco-badge { left: 22px; top: 248px; width: 50px; height: 50px; }
  .box-front .volume { left: 96px; top: 256px; font-size: 12px; }
</style>
</head>
<body>

<svg width="0" height="0" style="position:absolute" aria-hidden="true">
  <defs>
    <radialGradient id="bubble-fill" cx="35%" cy="35%" r="65%">
      <stop offset="0%" stop-color="#ffffff" stop-opacity="0.55"/>
      <stop offset="60%" stop-color="#c9c4ff" stop-opacity="0.25"/>
      <stop offset="100%" stop-color="#ffffff" stop-opacity="0.6"/>
    </radialGradient>
    <symbol id="bubble" viewBox="-10 -10 20 20">
      <circle r="9.4" fill="url(#bubble-fill)" stroke="#ffffff" stroke-opacity="0.7" stroke-width="0.6"/>
      <circle cx="-1.5" cy="1.5" r="4" fill="none" stroke="#ffffff" stroke-opacity="0.6" stroke-width="0.5"/>
    </symbol>
    <symbol id="sparkle" viewBox="-10 -10 20 20">
      <circle r="3" fill="#ffffff" opacity="0.4"/>
      <path d="M0,-10 Q0.8,-0.8 10,0 Q0.8,0.8 0,10 Q-0.8,0.8 -10,0 Q-0.8,-0.8 0,-10Z" fill="#ffffff"/>
    </symbol>
  </defs>
</svg>

  <section class="panel label-front" aria-label="Spray bottle front label">
    <svg class="decor" aria-hidden="true">
      <use href="#bubble" x="40" y="12" width="34" height="34"/>
      <use href="#bubble" x="3" y="116" width="54" height="54"/>
      <use href="#bubble" x="225" y="100" width="50" height="50"/>
      <use href="#bubble" x="212" y="212" width="20" height="20"/>
      <use href="#bubble" x="69" y="233" width="22" height="22"/>
      <use href="#sparkle" x="205" y="5" width="54" height="54"/>
      <use href="#sparkle" x="14" y="50" width="34" height="34"/>
    </svg>
    <div class="abs brand-name">Marlo</div>
    <div class="abs product-type">Stain Remove Spray</div>
    <div class="abs headline">I’ve got this</div>
    <div class="abs tagline">Get it dirty. Marlo will clean it.</div>
    <div class="eco-badge" role="img" aria-label="Eco friendly badge"></div>
    <div class="volume"><span class="volume-alt">8,5 oz</span><span class="volume-main">250 ml</span></div>
  </section>

  <section class="panel label-back" aria-label="Spray bottle back label">
    <svg class="decor" aria-hidden="true">
      <use href="#bubble" x="26" y="16" width="32" height="32"/>
      <use href="#bubble" x="20" y="226" width="22" height="22"/>
      <use href="#bubble" x="256" y="148" width="18" height="18"/>
      <use href="#sparkle" x="222" y="2" width="40" height="40"/>
      <use href="#sparkle" x="225" y="222" width="34" height="34"/>
    </svg>
    <div class="brand-name">Marlo</div>
    <div class="product-type">Stain Remove Spray</div>
    <p class="info-block first"><strong>Marlo stain remove Spray</strong> dolor sit amet, consectetuer adipiscing elit, sed diam nonummy nibh euismod tincidunt ut laoreet dolore magna aliquam erat volutpat. Ut wisi enim ad minim veniam, quis nostrud exerci tation ullamcorper suscipit lobortis nisl ut aliquip ex ea commodo conse-</p>
    <p class="info-block"><strong>Engredient</strong> dolor sit amet, consectetuer adipiscing elit, sed diam nonummy nibh euismod tincidunt ut laoreet dolore magna aliquam erat volutpat. Ut wisi enim ad minim veniam, quis nostrud exerci tation ullamcorper suscipit lobortis nisl ut aliquip ex ea commodo consequat. Duis</p>
    <p class="info-block"><strong>How to use</strong> dolor sit amet, consectetuer adipiscing elit, sed diam nonummy nibh euismod tincidunt ut laoreet dolore magna aliquam erat</p>
    <p class="info-block"><strong>Storage</strong> dolor sit amet, consectetuer adipiscing elit, sed diam nonummy nibh euismod tincidunt ut laoreet dolore magna aliquam erat volutpat.</p>
    <p class="info-block"><strong>Produced By :</strong> dolor sit amet</p>
  </section>

  <section class="panel box-top" aria-label="Wipes box top panel">
    <svg class="decor" aria-hidden="true">
      <use href="#bubble" x="14" y="14" width="30" height="30"/>
      <use href="#bubble" x="246" y="40" width="34" height="34"/>
      <use href="#bubble" x="10" y="110" width="30" height="30"/>
      <use href="#sparkle" x="228" y="0" width="44" height="44"/>
      <use href="#sparkle" x="40" y="2" width="28" height="28"/>
    </svg>
    <div class="abs brand-name">Marlo</div>
    <div class="abs product-type">Stain Remove Wipe</div>
    <div class="abs headline">I’ve got this</div>
    <div class="abs tagline">Get it dirty. Marlo will clean it.</div>
  </section>

  <section class="panel box-side" aria-label="Wipes box side panel">
    <svg class="decor" aria-hidden="true">
      <use href="#bubble" x="78" y="150" width="30" height="30"/>
      <use href="#bubble" x="8" y="250" width="16" height="16"/>
      <use href="#sparkle" x="80" y="270" width="34" height="34"/>
    </svg>
    <div class="brand-name">Marlo</div>
    <div class="product-type">Stain Remove Wipe</div>
    <p class="info-block first"><strong>Marlo stain remove wipe</strong> dolor sit amet, consectetuer adipiscing elit, sed diam nonummy nibh euismod tincidunt.</p>
    <p class="info-block"><strong>Engredient</strong> dolor sit amet, consectetuer adipiscing elit, sed diam nonummy nibh.</p>
    <p class="info-block"><strong>How to use</strong> dolor sit amet, consectetuer adipiscing elit.</p>
    <p class="info-block"><strong>Storage</strong> dolor sit amet, consectetuer adipiscing elit.</p>
    <p class="info-block"><strong>Produced By :</strong> dolor sit amet</p>
  </section>

  <section class="panel box-front" aria-label="Wipes box front panel">
    <svg class="decor" aria-hidden="true">
      <use href="#bubble" x="52" y="22" width="40" height="40"/>
      <use href="#bubble" x="0" y="178" width="56" height="56"/>
      <use href="#bubble" x="232" y="98" width="54" height="54"/>
      <use href="#bubble" x="232" y="230" width="20" height="20"/>
      <use href="#bubble" x="52" y="282" width="24" height="24"/>
      <use href="#sparkle" x="190" y="20" width="52" height="52"/>
      <use href="#sparkle" x="10" y="120" width="40" height="40"/>
    </svg>
    <div class="abs brand-name">Marlo</div>
    <div class="abs product-type">Stain Remove Wipe</div>
    <div class="abs headline">I’ve got this</div>
    <div class="abs tagline">Get it dirty. Marlo will clean it.</div>
    <div class="eco-badge" role="img" aria-label="Eco friendly badge"></div>
    <div class="volume"><span class="volume-alt">100 pc</span><span class="volume-main">200 sheet</span></div>
  </section>

</body>
</html>
```